Re-design of 4 x 2-sided reports

I need the 4 attached reports (3 are 2-sides of A4; 1 is 7-sides of A4) to be re-designed with a consistent look and feel. Just need 1 or 2 images per report being inserted plus consistent branding and contact details being displayed in the same location on each report with same colour, font and design). Reports are attached.
The reports are used as lead magnets.
That is, visitors to our website can download one of them (7 Steps To Sharpen Your Sales Pitch Before Spring Arrives) by filling in a form with their email address. Then over the next 30 days the other reports are sent to the subscriber via email autoresponders.
Blue Harbour Marketing is a marketing consultancy dealing with companies in the North West of England providing cost-effective and profitable marketing to small and medium-sized businesses that want better and quicker results. The reports need to be professional and corporate looking. Please let me know if you need any further clarification or have any questions. I attach an example report. I don't necessarily want to mirror this report (from the law firm) but it may help to understand what look I'm trying to get. Many thanks, Gordon

Target Market(s)

SMEs based in NW of England
Typically with turnover of £1m to £10m or 10 to 100 employees
Clients often in the construction sector, healthcare, accountants, lawyers and local councils.

Industry/Entity Type

Marketing

Font styles to use
Serif
Sans Serif

Colors
ec1f27

Requirements
Must have
• Consistent branding
• Logo in same place across all four reports
• Contact details in same place across all four reports
• Same font across all four reports
• Same colour across all four reports
• Professional and bold look
Nice to have
• Some strong stock photography
• 1 or 2 images per report
• More images for the 7-page report though
Should not have
• No graphics

```html
<!DOCTYPE html>
<html lang="en">
<head>
<meta charset="utf-8">
<title>7 Steps To Sharpen Your Sales Pitch Before Spring Arrives</title>
<link href="https://fonts.googleapis.com/css2?family=Oswald:wght@500;700&family=Roboto+Condensed:wght@400;700&family=Lato:wght@400;700&display=swap" rel="stylesheet">
<style>
  :root {
    --red: #ec1f27;
    --red-dark: #8e1a20;
    --ink: #2b2b2b;
    --body: #444;
    --bar: #e4e4e4;
    --stage: #d6d6d6;
    --white: #ffffff;
  }
  * { margin: 0; padding: 0; box-sizing: border-box; }
  html, body { width: 1200px; height: 848px; overflow: hidden; }
  body { background: var(--stage); font-family: "Lato", sans-serif; position: relative; }

  .page {
    position: absolute; top: 54px; width: 527px; height: 740px;
    background: var(--white); overflow: hidden;
    box-shadow: 0 6px 16px rgba(0,0,0,.25);
  }
  .page--front { left: 53px; }
  .page--back { left: 614px; }

  .hero { position: absolute; left: 0; top: 0; width: 527px; height: 300px; }

  .kicker {
    position: absolute; left: 22px; top: 22px;
    font-family: "Oswald", sans-serif; font-weight: 700; font-size: 50px;
    color: var(--white); letter-spacing: 1px; line-height: 1;
  }
  .title { position: absolute; left: 22px; top: 162px; }
  .title__big {
    font-family: "Oswald", sans-serif; font-weight: 700; font-size: 66px;
    color: var(--red); line-height: 1;
  }
  .title__line1 {
    font-family: "Roboto Condensed", sans-serif; font-size: 20px; color: var(--ink);
    margin-top: 6px; line-height: 1.1;
  }
  .title__line2 {
    font-family: "Roboto Condensed", sans-serif; font-weight: 700; font-size: 28px;
    color: var(--ink); line-height: 1.15;
  }
  .title__line2 em { font-style: normal; color: var(--red); }

  .step-head {
    position: absolute; height: 22px; background: var(--bar);
    border: 2px solid var(--red); border-left: none;
    font-family: "Lato", sans-serif; font-weight: 700; font-size: 12.5px;
    color: var(--ink); line-height: 18px; padding-left: 12px; white-space: nowrap;
  }
  .step-head--right { border-left: 2px solid var(--red); padding-left: 6px; }
  .step-head b { color: var(--red); font-weight: 700; }

  .step-body {
    position: absolute; font-size: 8.2px; line-height: 1.42; color: var(--body);
    text-align: justify;
  }
  .step-body ol { list-style: none; }
  .step-body .li-mark { color: var(--red); }
  .list-cols { display: flex; gap: 70px; margin-top: 4px; }

  .brand { position: absolute; display: flex; flex-direction: column; align-items: center; width: 110px; }
  .brand__mark { width: 48px; height: 48px; background: var(--red); }
  .brand__name {
    margin-top: 4px; font-family: "Lato", sans-serif; font-weight: 700;
    font-size: 10px; color: var(--red); text-align: center; line-height: 1.15;
  }

  .call {
    position: absolute; display: flex; align-items: center; gap: 4px;
    font-family: "Roboto Condensed", sans-serif; font-size: 15px; color: var(--ink);
  }
  .call__label { color: var(--red); font-weight: 700; }

  .footer { position: absolute; left: 0; bottom: 0; width: 100%; }
  .footer__email {
    height: 30px; background: var(--red-dark); color: var(--white);
    font-family: "Roboto Condensed", sans-serif; font-size: 12px;
    text-align: center; line-height: 30px;
  }
  .footer__web {
    height: 34px; background: var(--red); color: var(--white);
    font-family: "Lato", sans-serif; font-weight: 700; font-size: 11.5px;
    letter-spacing: 3.6px; text-align: center; line-height: 34px;
    border-top: 2px solid var(--white);
  }
</style>
</head>
<body>

<!-- Front page -->
<section class="page page--front">
  <svg class="hero" viewBox="0 0 527 300" aria-hidden="false">
    <defs>
      <linearGradient id="wood" x1="0" y1="0" x2="1" y2="1">
        <stop offset="0" stop-color="#7a4a3a"/>
        <stop offset=".6" stop-color="#5c3428"/>
        <stop offset="1" stop-color="#3f241c"/>
      </linearGradient>
      <clipPath id="frontClip">
        <path d="M0,0 H527 V150 C470,195 400,225 320,215 C220,200 110,125 0,138 Z"/>
      </clipPath>
    </defs>
    <rect width="527" height="240" fill="url(#wood)" clip-path="url(#frontClip)" role="img" aria-label="Photo of wooden figures on rising blocks with one figure lifted above the rest"/>
    <path d="M170,200 C300,250 430,215 527,150 V180 C430,245 300,262 170,200 Z" fill="var(--red)"/>
    <path d="M190,222 C320,262 440,230 527,190 V203 C440,245 320,272 190,222 Z" fill="var(--red-dark)"/>
    <path d="M230,238 C340,268 450,245 527,215 V222 C450,254 340,276 230,238 Z" fill="var(--red)"/>
  </svg>

  <div class="kicker">SUCCESS</div>

  <div class="title">
    <div class="title__big">7 Steps</div>
    <div class="title__line1">To Sharpen Your Sales Pitch</div>
    <div class="title__line2">Before <em>Spring Arrives</em></div>
  </div>

  <div class="step-head" style="left:0;top:312px;width:279px;"><b>1.</b> Review your existing customer database -</div>
  <p class="step-body" style="left:24px;top:350px;width:250px;">Can you cross sell other products or services to them? It's much cheaper to sell to your existing customers than try to find new customers. Can you upsell them i.e. to encourage them to purchase either more products, or products on a more frequent basis, or products of a greater total value?</p>

  <div class="step-head step-head--right" style="left:287px;top:312px;width:240px;"><b>3.</b> Get a marketing plan -</div>
  <p class="step-body" style="left:293px;top:350px;width:222px;">A list of marketing activity that can be undertaken month-by-month for 12 months. You will be amazed at how quickly you will reach the goals for your business with a marketing plan!</p>

  <div class="step-head" style="left:0;top:422px;width:279px;"><b>2.</b> Review your value proposition -</div>
  <p class="step-body" style="left:24px;top:460px;width:250px;">i.e. what value do you offer your customers? List all the benefits of your products, services and your business offers customers and how these differ from your competitors. Put these benefits in your sales and corporate literature, on your website and in your social media profiles. Make sure your sales team knows these benefits by heart!</p>

  <div class="step-head step-head--right" style="left:287px;top:422px;width:240px;"><b>4.</b> Optimise your website -</div>
  <p class="step-body" style="left:293px;top:460px;width:222px;">To increase the number of visitors to it, in order to increase the probability that people will engage with your business and eventually become customers</p>

  <div class="step-head" style="left:0;top:552px;width:279px;"><b>4.</b> Optimise your website -</div>
  <p class="step-body" style="left:24px;top:590px;width:250px;">More people now search the internet via their mobile phone or tablet than a PC or laptop! Research shows that consumers are more likely to buy from a business with a mobile friendly website than one that only has a standard website</p>

  <div class="brand" style="left:359px;top:525px;">
    <div class="brand__mark"></div>
    <div class="brand__name">Blue Harbour Marketing</div>
  </div>

  <div class="call" style="left:335px;top:614px;">
    <svg width="14" height="14" viewBox="0 0 24 24" aria-hidden="true"><circle cx="12" cy="12" r="10.5" fill="none" stroke="var(--red)" stroke-width="2"/><path d="M8.5 6.5l2 2.2-1.2 1.6c.8 1.7 2 2.9 3.6 3.7l1.6-1.2 2.2 2-1.1 2c-4.3-.3-8.4-4.4-8.6-8.7z" fill="var(--red)"/></svg>
    <span class="call__label">CALL:</span><span>01632 960 418</span>
  </div>

  <footer class="footer">
    <div class="footer__email">info@blueharbourmarketing.co.uk</div>
    <div class="footer__web">www.blueharbourmarketing.co.uk</div>
  </footer>
</section>

<!-- Back page -->
<section class="page page--back">
  <svg class="hero" viewBox="0 0 527 300">
    <defs>
      <linearGradient id="desk" x1="0" y1="0" x2="1" y2="1">
        <stop offset="0" stop-color="#1d3f86"/>
        <stop offset=".55" stop-color="#5b79b4"/>
        <stop offset="1" stop-color="#c9d3e6"/>
      </linearGradient>
    </defs>
    <rect width="527" height="182" fill="url(#desk)" role="img" aria-label="Photo of a hand writing on documents beside a tablet on a desk"/>
    <path d="M270,0 H527 V230 C500,120 420,40 270,0 Z" fill="var(--red)"/>
    <path d="M250,0 H275 C410,35 495,110 527,200 V230 C490,120 400,35 250,0 Z" fill="var(--white)"/>
    <path d="M285,0 C420,40 500,115 527,180 V190 C495,120 415,45 285,0 Z" fill="var(--red-dark)"/>
  </svg>

  <div class="step-head" style="left:0;top:158px;width:202px;"><b>6.</b> Embrace social media -</div>
  <div class="step-body" style="left:26px;top:194px;width:480px;">
    <p>it's here to stay and those businesses, even small and medium-sized businesses, that choose to ignore social media will be left behind in the near future</p>
    <div class="list-cols">
      <ol>
        <li><span class="li-mark">a.</span> Set up a Friendsbook Page (not profile)</li>
        <li><span class="li-mark">b.</span> Set up a SearchCircle Page</li>
        <li><span class="li-mark">c.</span> Set up a company Chirper account</li>
      </ol>
      <ol>
        <li><span class="li-mark">d.</span> Set up a ProLink Company Profile</li>
        <li><span class="li-mark">e.</span> Start to use all of the above</li>
      </ol>
    </div>
  </div>

  <div class="step-head" style="left:0;top:266px;width:180px;"><b>7.</b> Image is all -</div>
  <p class="step-body" style="left:26px;top:296px;width:486px;">get your branding, corporate literature, sales literature, exhibition materials and website reviewed - professionally - and re-designed to be congruent with who you are as a company and how you want to position your company in the minds of your existing customers and potential customers</p>

  <div class="step-head" style="left:0;top:349px;width:290px;"><b>8.</b> Explore video marketing -</div>
  <p class="step-body" style="left:26px;top:381px;width:486px;">the number of videos watched on ViewStream and other video channels such as ClipVault will blow your mind. The benefits of video marketing are massive: more traffic to your website, higher profile and awareness of your business, greater credibility and authority, and the biggest, free way to expose your business to your existing and potential customers there is, bar none!</p>

  <div class="step-head" style="left:0;top:442px;width:310px;"><b>9.</b> If you don't sell via the internet, you should -</div>
  <p class="step-body" style="left:26px;top:475px;width:486px;">Virtually all businesses can benefit massively from a 'shop on the internet'. Initially, some businesses start via BidMarket or LocalSwap but eventually need their own e-commerce website.</p>

  <div class="step-head" style="left:0;top:511px;width:520px;"><b>10.</b> Commit to investing time and some resources into regular marketing activity -</div>
  <p class="step-body" style="left:26px;top:545px;width:486px;">preferably from a marketing plan. Generally, it's quicker, easier and far more affordable to outsource your marketing than employ someone in-house, at least initially. You will be surprised how quickly regular, focused marketing brings results.</p>

  <div class="call" style="left:216px;top:616px;">
    <svg width="14" height="14" viewBox="0 0 24 24" aria-hidden="true"><circle cx="12" cy="12" r="10.5" fill="none" stroke="var(--red)" stroke-width="2"/><path d="M8.5 6.5l2 2.2-1.2 1.6c.8 1.7 2 2.9 3.6 3.7l1.6-1.2 2.2 2-1.1 2c-4.3-.3-8.4-4.4-8.6-8.7z" fill="var(--red)"/></svg>
    <span class="call__label">CALL:</span><span>01632 960 418</span>
  </div>

  <div class="brand" style="left:400px;top:586px;">
    <div class="brand__mark"></div>
    <div class="brand__name">Blue Harbour Marketing</div>
  </div>

  <footer class="footer">
    <div class="footer__email">info@blueharbourmarketing.co.uk</div>
    <div class="footer__web">www.blueharbourmarketing.co.uk</div>
  </footer>
</section>

</body>
</html>
```